Flyer für ein Jugendfestival
Zielgruppe
Wir sind ein christlicher Jugendverband, der hauptsächlich Freizeiten organisiert. Die Haupt-Zielgruppe sind somit Jugendliche im Alter von 13-17 Jahre, darüber hinaus junge Erwachsene im Alter von 18-25. Viele haben einen christlichen Kontext, viele allerdings nicht. Gemein haben alle, dass sie im Sommer unterwegs waren.
Aufgabenstellung
Der Flyer ist für das 'Grasp the Lantern', unser Jugendfestival, dieses findet vom 15.-17. September 2023 statt. Motto: 'nah.dran' Ort: Altbirkenfelde. Preis: 74€. Alter: ab 13 Jahre.
Mögliche Farbgebung in Richtung: rosa, flieder, blau oder grün (nicht allzu bunt, farblich stimmig). Inhaltlicher Schwerpunkt ist Sicherheit, muss aber nicht wörtlich vorkommen.
Es müssen keine realen Bilder vorkommen, sondern gern auch nur Silhouetten oder Farbverläufe...
Idee für die Aufteilung: Vorderseite: Daten, Rückseite: Aktionen und Teaser der Bands (Workshops, Jesus erleben, Worship, Lounge, Döner, Funkenhain-Ensemble, Morgen wird bunter... ) Kann aber auch abweichen, da gerade noch nicht alle Acts feststehen
Somit soll der Flyer für Jugendliche ansprechend wirken, möglichst alle repräsentieren (also nicht nur eine Person, sondern mehrere oder gar keine), 'in sein' und mit dem Trend gehen.

```html
<!DOCTYPE html>
<html lang="de">
<head>
<meta charset="utf-8">
<title>Grasp the Lantern – Flyer</title>
<link href="https://fonts.googleapis.com/css2?family=Barlow+Condensed:wght@400;500;600&family=Roboto+Condensed:wght@400;500&display=swap" rel="stylesheet">
<style>
  :root {
    --stage: #727271;
    --paper: #ffffff;
    --navy: #0d3a4e;
    --white: #ffffff;
    --cream: #efe9df;
  }
  * { margin: 0; padding: 0; box-sizing: border-box; }
  html, body { width: 1200px; height: 848px; overflow: hidden; background: var(--stage); }
  .flyer {
    position: absolute; top: 72px; width: 361px; height: 722px;
    background: var(--paper); overflow: hidden;
    font-family: "Barlow Condensed", "Roboto Condensed", sans-serif;
  }
  .flyer--front { left: 81px; }
  .flyer--back { left: 509px; }

  .paint { position: absolute; inset: 0; }
  .flyer--front .paint {
    background:
      radial-gradient(ellipse 45% 30% at 72% 52%, rgba(74,160,210,.85), transparent 70%),
      radial-gradient(ellipse 40% 25% at 30% 62%, rgba(246,190,40,.8), transparent 70%),
      radial-gradient(ellipse 50% 22% at 55% 82%, rgba(210,45,20,.85), transparent 70%),
      linear-gradient(180deg, var(--paper) 0%, var(--paper) 28%, var(--cream) 45%, #f1c34a 75%, #e5781c 90%, #d63a18 100%);
  }
  .flyer--back .paint {
    background:
      radial-gradient(ellipse 30% 18% at 10% 44%, rgba(90,180,225,.8), transparent 70%),
      radial-gradient(ellipse 35% 22% at 80% 72%, rgba(215,55,25,.75), transparent 70%),
      radial-gradient(ellipse 45% 18% at 40% 85%, rgba(110,180,220,.55), transparent 70%),
      linear-gradient(180deg, var(--paper) 0%, var(--paper) 38%, #f6f3ee 58%, #efd79b 82%, #eba33a 94%, #d5451d 100%);
  }

  .title {
    position: absolute; left: 42px; top: 68px;
    color: var(--navy); font-weight: 600; font-size: 62px; line-height: 55px;
    letter-spacing: 5px; text-transform: uppercase;
  }
  .brand {
    position: absolute; left: 294px; top: 20px;
    writing-mode: vertical-rl; transform: rotate(180deg);
    font-weight: 600; font-size: 24px; letter-spacing: 1px; color: var(--navy);
  }
  .vertical {
    position: absolute; writing-mode: vertical-rl; transform: rotate(180deg); white-space: nowrap;
  }
  .dates { left: 38px; bottom: 40px; color: var(--white); font-size: 50px; font-weight: 500; line-height: 1; }
  .month { left: 44px; bottom: 170px; color: var(--navy); font-family: "Roboto Condensed", sans-serif; font-size: 30px; line-height: 1; }
  .date-rule { position: absolute; left: 0; top: 577px; width: 56px; height: 3px; background: var(--white); }
  .date-tick { position: absolute; left: 54px; top: 555px; width: 3px; height: 25px; background: var(--white); }

  .motto { position: absolute; right: 14px; top: 624px; color: var(--white); font-size: 46px; font-weight: 500; letter-spacing: 1px; line-height: 1; white-space: nowrap; }
  .facts { position: absolute; right: 22px; top: 679px; color: var(--white); font-size: 14px; white-space: nowrap; }

  .motto-vertical { left: 36px; top: 68px; color: var(--navy); font-family: "Roboto Condensed", sans-serif; font-weight: 500; font-size: 62px; line-height: 1; }
  .chevrons { position: absolute; left: 122px; top: 74px; }
  .program { position: absolute; left: 122px; top: 150px; color: var(--navy); font-size: 22px; line-height: 27px; list-style: none; }
  .contact { position: absolute; right: 42px; top: 614px; color: var(--white); font-size: 14.5px; line-height: 19px; text-align: right; white-space: nowrap; }
  .social { position: absolute; right: 42px; top: 670px; color: var(--white); font-size: 14.5px; display: flex; align-items: center; gap: 6px; }
  .social-dot { width: 8px; height: 8px; border-radius: 50%; background: var(--white); }
</style>
</head>
<body>
  <section class="flyer flyer--front">
    <div class="paint" role="img" aria-label="Abstrakte Farbspritzer in Blau, Gelb, Orange und Rot, die von unten aufsteigen"></div>
    <h1 class="title">Grasp<br>the<br>Lantern</h1>
    <div class="brand">LICHTWEG</div>
    <div class="vertical month">september 2023</div>
    <div class="date-rule"></div>
    <div class="date-tick"></div>
    <div class="vertical dates">15-17.</div>
    <div class="motto">‚nah.dran‘</div>
    <div class="facts">Altbirkenfelde | ab 13 Jahre | Preis: 74€</div>
  </section>

  <section class="flyer flyer--back">
    <div class="paint" role="img" aria-label="Abstrakte Farbspritzer in Hellblau, Gelb und Rot auf hellem Grund"></div>
    <div class="vertical motto-vertical">nah.dran</div>
    <svg class="chevrons" width="62" height="34" viewBox="0 0 62 34" aria-hidden="true">
      <polyline points="3,3 28,17 3,31" fill="none" stroke="#0d3a4e" stroke-width="6"/>
      <polyline points="33,3 58,17 33,31" fill="none" stroke="#0d3a4e" stroke-width="6"/>
    </svg>
    <ul class="program">
      <li>workshops | jesus erleben</li>
      <li>worship | lounge | döner</li>
      <li>funkenhain-ensemble</li>
      <li>morgen wird bunter...uvm...</li>
    </ul>
    <div class="contact">infos &amp; anmeldung unter:<br>jonas beispiel | 0123 98765 | mail@jonas-beispiel.de</div>
    <div class="social">find us on @lichtweg <span class="social-dot"></span></div>
  </section>
</body>
</html>
```